One-page magazine ad for accountant serving the non-profit industry

I am Certified Public Accountant placing a one-page ad in Lanternway Journal. The ad will be seen by churches and other non-profit organizations.
Lanternway Journal requires the following:
Accepted file formats:
a) Press ready PDF with all fonts embedded. OR
b) Flattened CMYK Abode Photoshop PSD or illustrator PDF or EPS with all fonts outlined.
Ad Specs:
Trim 8" x 10.5"
Live 7.5" x 10"
Bleed 8.25" x 10.75"

I would like the ad to state the following information:

Marcus T. Quillby, CPA, CGMA

I am Certified Public Accountant with over 30 years of experience serving the accounting and tax needs of churches and non-profit organizations.

Some of the services I can offer:

Audits, Reviews, Compilations
Bookkeeping Services
Payroll Taxes
501C3 - IRS exemption applications
Clergy Housing Allowance issues and Personal Taxes

```html
<!DOCTYPE html>
<html lang="en">
<head>
<meta charset="utf-8">
<title>Marcus T. Quillby, CPA, CGMA – Ad</title>
<link href="https://fonts.googleapis.com/css2?family=Arimo:wght@400;700&family=Cabin:wght@400;500&display=swap" rel="stylesheet">
<style>
  :root {
    --slate: #566573;
    --ink: #1c1c1c;
    --paper: #ffffff;
    --olive: #b3b035;
    --olive-soft: #8f8f45;
  }
  html, body {
    margin: 0;
    padding: 0;
    overflow: hidden;
    background: var(--paper);
  }
  .ad {
    position: relative;
    width: 921px;
    height: 1200px;
    overflow: hidden;
    background: var(--paper);
    font-family: "Cabin", "Gill Sans", sans-serif;
    color: var(--ink);
  }
  .ad__panel {
    position: absolute;
    left: 0; top: 0;
    width: 921px;
    height: 857px;
    background: var(--slate);
  }
  .ad__title {
    position: absolute;
    left: 0; top: 56px;
    width: 100%;
    margin: 0;
    text-align: center;
    font-family: "Arimo", Arial, sans-serif;
    font-weight: 400;
    font-size: 56px;
    line-height: 76px;
    letter-spacing: 1px;
    color: var(--paper);
  }
  .ad__rule {
    position: absolute;
    left: 118px; top: 226px;
    width: 697px;
    height: 4px;
    background: var(--ink);
  }
  .ad__intro {
    position: absolute;
    left: 110px; top: 274px;
    width: 700px;
    margin: 0;
    text-align: center;
    font-size: 30px;
    line-height: 40px;
  }
  .ad__emblem {
    position: absolute;
    left: 651px; top: 442px;
    width: 270px;
    height: 263px;
    border-radius: 50% 0 0 50%;
    background: radial-gradient(circle at 50% 50%, var(--olive) 0%, var(--olive-soft) 55%, var(--slate) 72%);
    opacity: 0.8;
  }
  .ad__services-title {
    position: absolute;
    left: 88px; top: 536px;
    margin: 0;
    font-family: "Arimo", Arial, sans-serif;
    font-weight: 700;
    font-size: 31px;
    line-height: 40px;
  }
  .ad__services {
    position: absolute;
    left: 86px; top: 598px;
    margin: 0;
    padding: 0;
    list-style: none;
    font-size: 30px;
    line-height: 43px;
  }
  .ad__services li::before { content: "•"; }
  .ad__brand {
    position: absolute;
    left: 130px; top: 900px;
    width: 190px;
    text-align: center;
  }
  .ad__brand-name {
    display: block;
    height: 100px;
    line-height: 100px;
    font-size: 38px;
    font-weight: 500;
    color: var(--ink);
  }
  .ad__brand-rule {
    width: 128px;
    height: 3px;
    margin: 20px auto 18px;
    background: var(--ink);
  }
  .ad__brand-tag {
    margin: 0;
    font-family: "Arimo", Arial, sans-serif;
    font-size: 25px;
    line-height: 36px;
  }
  .ad__divider {
    position: absolute;
    left: 405px; top: 927px;
    width: 3px;
    height: 217px;
    background: var(--ink);
  }
  .ad__contact {
    position: absolute;
    left: 440px; top: 968px;
    width: 440px;
    margin: 0;
    text-align: center;
    font-style: normal;
    font-size: 25px;
    line-height: 37px;
  }
</style>
</head>
<body>
  <main class="ad">
    <section class="ad__panel">
      <h1 class="ad__title">MARCUS T. QUILLBY<br>CPA, CGMA</h1>
      <div class="ad__rule"></div>
      <p class="ad__intro">I am a Certified Public Accountant with over 30 years of experience serving accounting and tax needs of churches and non-profit organizations.</p>
      <div class="ad__emblem" role="img" aria-label="Laurel wreath encircling balance scales emblem"></div>
      <h2 class="ad__services-title">Some of the services I can offer:</h2>
      <ul class="ad__services">
        <li>Audits, Reviews, Compilations</li>
        <li>Bookkeeping Services</li>
        <li>Payroll Taxes</li>
        <li>501C3 - IRS exemption applications</li>
        <li>Clergy Housing Allowance issues and Personal Taxes</li>
      </ul>
    </section>

    <div class="ad__brand">
      <span class="ad__brand-name">Quillby</span>
      <div class="ad__brand-rule"></div>
      <p class="ad__brand-tag">certified<br>public<br>accountant</p>
    </div>
    <div class="ad__divider"></div>
    <address class="ad__contact">
      Marcus T. Quillby, CPA, CGMA<br>
      email: marcus@quillbycpa.com<br>
      telephone: (555) 314-2096
    </address>
  </main>
</body>
</html>
```